Flyer needed For the Council for Stewardship of Public Works

With an increasing need for professional staffing in our design and construction industry it is important for organizations to be able to attract, support, and retain people of all genders. With the increase of women entering the design/construction industry, we need to be able to identify and address the specific needs of women in our industry, including those A/E’s who are on the facility Owner side.

This Forum will provide a venue to openly discuss the issues affecting our industry and ideas to address those issues.The program includes time for presentations and a panel discussion by accomplished women in our industry, and facilitated table and open discussions to form solutions with your peers. You will come away with ideas you can implement within your organization to build processes and a supportive culture for women

IN THE ATTACHMENTS
* you'll find our company logo

Target Market(s)

Women in the design and construction industry

Industry/Entity Type

Construction

Requirements
Must have
• Logo, event name, date, time, location, panelists names and pics, NBF continuing education provided, contact information: Maren Holtzclaw, maren.holtzclaw@c-sfpw.org, (555) 740-1938
• Register at: www.c-sfpw.org/events
• Design should encompass the description given above.
Nice to have
• Colors that compliment our logo

```html
<!DOCTYPE html>
<html lang="en">
<head>
<meta charset="utf-8">
<title>Women in Design &amp; Construction Forum – Council for Stewardship of Public Works</title>
<link rel="stylesheet" href="https://fonts.googleapis.com/css2?family=Oswald:wght@400;700&family=Open+Sans:wght@400;700&display=swap">
<style>
  :root {
    --paper: #ffffff;
    --ink: #333333;
    --role-blue: #1e3c8c;
    --role-green: #5fa12b;
    --role-lime: #97bb2a;
    --role-teal: #2b8c97;
    --muted: #666666;
    --badge: #2f6fb3;
    --photo: #c9d3dc;
  }
  * { margin: 0; padding: 0; box-sizing: border-box; }
  html, body { width: 849px; height: 1200px; overflow: hidden; background: var(--paper); }
  .flyer {
    position: relative;
    width: 849px;
    height: 1200px;
    background: var(--paper);
    color: var(--ink);
  }

  .event {
    position: absolute;
    left: 34px;
    top: 48px;
    right: 34px;
  }
  .event-name {
    font-family: "Oswald", sans-serif;
    font-weight: 700;
    font-size: 50px;
    line-height: 60px;
    color: var(--role-blue);
    letter-spacing: -0.5px;
  }
  .event-details {
    margin-top: 14px;
    font-family: "Open Sans", sans-serif;
    font-size: 21px;
    line-height: 32px;
    color: var(--ink);
  }
  .event-details strong { color: var(--role-teal); }

  .roles {
    position: absolute;
    left: 34px;
    top: 246px;
    list-style: none;
  }
  .role {
    font-family: "Oswald", sans-serif;
    font-size: 42px;
    line-height: 76px;
    white-space: nowrap;
    letter-spacing: -0.5px;
  }
  .role-title { font-weight: 700; margin-right: 10px; }
  .role-name { font-weight: 400; color: var(--ink); }
  .role-name--strong { font-weight: 700; }
  .role-link {
    font-family: "Oswald", sans-serif;
    font-size: 15px;
    color: var(--muted);
    margin-left: 10px;
  }
  .role-note { font-size: 18px; font-weight: 400; color: var(--muted); margin-left: 6px; }
  .role--mc .role-title { color: var(--role-blue); }
  .role--scribe .role-title { color: var(--role-green); }
  .role--visual .role-title { color: var(--role-lime); }
  .role--panel .role-title { color: var(--role-teal); }

  .panelists {
    position: absolute;
    left: 34px;
    top: 566px;
    list-style: none;
    font-family: "Open Sans", sans-serif;
    font-size: 29px;
    line-height: 56px;
    white-space: nowrap;
  }
  .panelist-role { font-weight: 700; color: var(--ink); margin-right: 14px; }
  .panelist-name { font-weight: 400; color: var(--ink); }

  .panel-photos {
    position: absolute;
    left: 34px;
    right: 34px;
    top: 866px;
    display: flex;
    justify-content: space-between;
    list-style: none;
  }
  .panel-photo { width: 130px; text-align: center; }
  .panel-photo .portrait {
    display: block;
    width: 92px;
    height: 92px;
    margin: 0 auto;
    border-radius: 50%;
    background: linear-gradient(160deg, #dde4ea, var(--photo));
  }
  .panel-photo .caption {
    display: block;
    margin-top: 6px;
    font-family: "Oswald", sans-serif;
    font-size: 16px;
    color: var(--role-teal);
  }

  .contact {
    position: absolute;
    left: 34px;
    right: 34px;
    top: 1012px;
    font-family: "Open Sans", sans-serif;
    font-size: 19px;
    line-height: 30px;
    color: var(--ink);
  }
  .contact strong { color: var(--role-blue); }

  .org-mark {
    position: absolute;
    left: 22px;
    bottom: 26px;
    display: flex;
    align-items: center;
    gap: 10px;
    font-family: "Open Sans", sans-serif;
    font-weight: 700;
    font-size: 14px;
    color: var(--badge);
    width: 280px;
  }
  .org-mark .dot { width: 60px; height: 60px; border-radius: 50%; background: var(--badge); flex: none; }
  .ce-mark {
    position: absolute;
    right: 22px;
    bottom: 32px;
    display: flex;
    align-items: center;
    gap: 8px;
    font-family: "Open Sans", sans-serif;
    font-weight: 700;
    font-size: 22px;
    color: var(--ink);
  }
  .ce-mark .square { width: 34px; height: 34px; background: var(--ink); }
</style>
</head>
<body>
<main class="flyer">
  <header class="event">
    <h1 class="event-name">Women in Design &amp; Construction Forum</h1>
    <p class="event-details"><strong>Thursday, March 12</strong> · 8:00 AM – 12:30 PM</p>
    <p class="event-details">Riverside Conference Center · 400 Harbor Lane, Suite 2</p>
  </header>

  <ul class="roles">
    <li class="role role--mc"><span class="role-title">Master of Ceremonies</span><span class="role-name">Dana Kowalczyk</span></li>
    <li class="role role--scribe"><span class="role-title">Scribe</span><span class="role-name">Maren Holtzclaw</span></li>
    <li class="role role--visual"><span class="role-title">Visual Note Taking</span><span class="role-name">Tessa Marlowe</span><span class="role-link">http://tessamarlowe.example/connect</span></li>
    <li class="role role--panel"><span class="role-title">Panel</span><span class="role-name role-name--strong">Moderator - Ruth Ellery</span><span class="role-note">(Beacon Construction)</span></li>
  </ul>

  <ul class="panelists">
    <li><span class="panelist-role">Architect</span><span class="panelist-name">Lena Varga Architects</span></li>
    <li><span class="panelist-role">Engineer</span><span class="panelist-name">?? Hollis-Brandt</span></li>
    <li><span class="panelist-role">Contractor</span><span class="panelist-name">Nadia Ferraro (Ferraro Brothers)</span></li>
    <li><span class="panelist-role">Owner</span><span class="panelist-name">Imogen Price (State Univ. Facilities Office)</span></li>
    <li><span class="panelist-role">Sub/trade</span><span class="panelist-name">??</span></li>
  </ul>

  <ul class="panel-photos">
    <li class="panel-photo"><span class="portrait" role="img" aria-label="Portrait photo of moderator Ruth Ellery"></span><span class="caption">Moderator</span></li>
    <li class="panel-photo"><span class="portrait" role="img" aria-label="Portrait photo of the architect panelist"></span><span class="caption">Architect</span></li>
    <li class="panel-photo"><span class="portrait" role="img" aria-label="Portrait photo of the engineer panelist"></span><span class="caption">Engineer</span></li>
    <li class="panel-photo"><span class="portrait" role="img" aria-label="Portrait photo of contractor Nadia Ferraro"></span><span class="caption">Contractor</span></li>
    <li class="panel-photo"><span class="portrait" role="img" aria-label="Portrait photo of owner Imogen Price"></span><span class="caption">Owner</span></li>
  </ul>

  <section class="contact">
    <p><strong>Register at:</strong> www.c-sfpw.org/events · NBF continuing education provided</p>
    <p><strong>Contact:</strong> Maren Holtzclaw · maren.holtzclaw@c-sfpw.org · (555) 740-1938</p>
  </section>

  <div class="org-mark"><span class="dot"></span><span>Council for Stewardship of Public Works</span></div>
  <div class="ce-mark"><span class="square"></span><span>NBF</span></div>
</main>
</body>
</html>
```